Morvela Aesthetic Doctor

I require an elegant, luxurious looking business card for my aesthetic business. I am a doctor and that will set me aside from competitors. I am planning to provide home and spa based treatments to clients with high expectations. I have attached my logo.

```html
<!DOCTYPE html>
<html lang="en">
<head>
<meta charset="utf-8">
<title>Morvela Aesthetic Doctor – Business Card</title>
<link href="https://fonts.googleapis.com/css2?family=Crimson+Text:wght@400;600;700&display=swap" rel="stylesheet">
<style>
  :root {
    --page-bg: #f5f5f5;
    --card-dark: #212121;
    --band-grey: #404040;
    --card-white: #ffffff;
    --ink: #1a1a1a;
    --text-body: #2b2b2b;
    --logo-grey: #c9c9c9;
    --accent-blue: #3d9fdc;
    --tagline: #f2f2f2;
  }
  * { margin: 0; padding: 0; box-sizing: border-box; }
  html, body {
    width: 1200px; height: 2291px; overflow: hidden;
    background: var(--page-bg);
    font-family: "Crimson Text", Georgia, serif;
  }
  .canvas { position: relative; width: 1200px; height: 2291px; }

  .card {
    position: absolute; left: 135px; width: 930px; height: 531px;
    box-shadow: 0 3px 8px rgba(0,0,0,0.35);
    overflow: hidden;
  }
  .card--front { top: 581px; background: var(--card-dark); }
  .card--back  { top: 1179px; background: var(--card-white); }

  .pattern-field {
    position: absolute; left: 0; width: 100%;
    background: var(--card-dark);
  }

  /* Front */
  .front-band {
    position: absolute; left: 0; top: 155px; width: 100%; height: 222px;
    background: var(--band-grey);
    display: flex; flex-direction: column; align-items: center; justify-content: center;
  }
  .brand {
    display: flex; align-items: center; gap: 18px;
  }
  .brand__dot {
    width: 22px; height: 22px; border-radius: 50%;
    background: var(--accent-blue); flex: none;
  }
  .brand__name {
    font-weight: 400; color: var(--logo-grey); line-height: 1;
    white-space: nowrap;
  }
  .front-band .brand__name { font-size: 46px; }
  .tagline {
    margin-top: 34px;
    font-size: 23px; letter-spacing: 0.5px; color: var(--tagline);
  }

  /* Back */
  .back-panel {
    position: absolute; left: 0; top: 0; width: 412px; height: 100%;
    background: var(--card-dark);
  }
  .back-panel .brand {
    position: absolute; left: 0; top: 0; width: 100%; height: 100%;
    justify-content: center; gap: 12px;
  }
  .back-panel .brand__name { font-size: 27px; }
  .back-panel .brand__dot { width: 16px; height: 16px; }
  .divider {
    position: absolute; left: 417px; top: 0; width: 6px; height: 100%;
    background: var(--ink);
  }
  .details { position: absolute; left: 486px; top: 0; right: 30px; color: var(--text-body); }
  .person {
    position: absolute; top: 76px; white-space: nowrap;
    font-size: 37px; font-weight: 700; color: var(--ink);
  }
  .person__post { font-size: 16px; font-weight: 400; margin-left: 14px; letter-spacing: 0.3px; }
  .qualification { position: absolute; top: 133px; font-size: 23px; white-space: nowrap; }
  .contacts { position: absolute; top: 196px; list-style: none; }
  .contacts li {
    display: flex; align-items: center; height: 39px;
    font-size: 22px; letter-spacing: 0.4px; white-space: nowrap;
  }
  .contacts svg { width: 20px; height: 20px; margin-right: 17px; fill: var(--accent-blue); }
  .services {
    position: absolute; top: 367px; width: 420px;
    font-size: 19px; line-height: 26px;
  }
</style>
</head>
<body>
<main class="canvas">

  <section class="card card--front" aria-label="Business card front">
    <div class="pattern-field" style="top:0;height:155px" role="img" aria-label="Subtle dark geometric triangle pattern"></div>
    <div class="front-band">
      <div class="brand">
        <span class="brand__dot"></span>
        <span class="brand__name">Morvela Aesthetic Doctor</span>
      </div>
      <p class="tagline">HOME AND SPA BASED TREATMENTS</p>
    </div>
    <div class="pattern-field" style="top:377px;height:154px" role="img" aria-label="Subtle dark geometric triangle pattern"></div>
  </section>

  <section class="card card--back" aria-label="Business card back">
    <div class="back-panel" role="img" aria-label="Dark panel with subtle geometric triangle pattern">
      <div class="brand">
        <span class="brand__dot"></span>
        <span class="brand__name">Morvela Aesthetic Doctor</span>
      </div>
    </div>
    <div class="divider"></div>

    <div class="details">
      <h1 class="person">Dr Elise Varnholt<span class="person__post">MRCPCH MD</span></h1>
      <p class="qualification">Australasian Diploma of Aesthetic Medicine</p>
      <ul class="contacts">
        <li>
          <svg viewBox="0 0 24 24" aria-hidden="true"><path d="M6.6 10.8a15.1 15.1 0 0 0 6.6 6.6l2.2-2.2c.3-.3.7-.4 1-.2 1.1.4 2.3.6 3.6.6.6 0 1 .4 1 1V20c0 .6-.4 1-1 1A17 17 0 0 1 3 4c0-.6.4-1 1-1h3.5c.6 0 1 .4 1 1 0 1.3.2 2.5.6 3.6.1.3 0 .7-.2 1z"/></svg>
          0800 555 014
        </li>
        <li>
          <svg viewBox="0 0 24 24" aria-hidden="true"><path d="M2 5h20v14H2z M3.5 6.5 12 13l8.5-6.5" fill="var(--accent-blue)"/><path d="M3 6l9 7 9-7" fill="none" stroke="#fff" stroke-width="1.6"/></svg>
          elise@morvela.co.nz
        </li>
        <li>
          <svg viewBox="0 0 24 24" aria-hidden="true"><path d="M12 2a10 10 0 1 0 0 20 10 10 0 0 0 0-20zm6.9 6h-3a15 15 0 0 0-1.3-3.9A8 8 0 0 1 18.9 8zM12 4c.8 1.2 1.5 2.5 1.9 4h-3.8c.4-1.5 1.1-2.8 1.9-4zM4.3 14a8 8 0 0 1 0-4h3.4a16 16 0 0 0 0 4zm.8 2h3a15 15 0 0 0 1.3 3.9A8 8 0 0 1 5.1 16zm3-8h-3a8 8 0 0 1 4.3-3.9C8.8 5.3 8.4 6.6 8.1 8zM12 20c-.8-1.2-1.5-2.5-1.9-4h3.8c-.4 1.5-1.1 2.8-1.9 4zm2.3-6H9.7a14 14 0 0 1 0-4h4.6a14 14 0 0 1 0 4zm.3 5.9c.6-1.2 1-2.5 1.3-3.9h3a8 8 0 0 1-4.3 3.9zM16.3 14a16 16 0 0 0 0-4h3.4a8 8 0 0 1 0 4z"/></svg>
          www.morvela.co.nz
        </li>
      </ul>
      <p class="services">Dermal injectables - Plasma facials - Microneedling Skin boosters - Excessive sweating Home and Spa Based Treatments</p>
    </div>
  </section>

</main>
</body>
</html>
```